11 x 11 Flyer Design for Social Media - Reverse Mortgages

62 or older?

A Reverse Mortgage
could be
Your Road to Financial Freedom

* No Monthly Payments
* No Income Requirements
* No Credit Score Requirements
* No Loss of Ownership

Receive cash by lump sum, monthly installments or a line of credit!!

Call us today for a Free Consultation!!
(800) 471-2965

Bluegate Financial Services, Inc.
NMLS #318760
www.bluegatehome.com

```html
<!DOCTYPE html>
<html lang="en">
<head>
<meta charset="utf-8">
<title>Reverse Mortgage Flyer – Bluegate Financial Services</title>
<link href="https://fonts.googleapis.com/css2?family=Luckiest+Guy&family=Arimo:ital,wght@0,400;0,700;1,700&display=swap" rel="stylesheet">
<style>
  :root {
    --band-grey: #a9a9a9;
    --footer-grey: #b3b3b3;
    --footer-dark: #2b2727;
    --footer-stripe: #d9d9d9;
    --ink: #111111;
    --accent-red: #e8141b;
    --list-ink: #14141c;
    --tick-blue: #2b4fa8;
    --cash-ink: #1d3636;
    --white: #ffffff;
    --sky-light: #fdf8e2;
    --sky-warm: #f6e7a8;
    --sand: #e9cf8c;
  }
  * { margin: 0; padding: 0; box-sizing: border-box; }
  html, body { width: 1200px; height: 1200px; overflow: hidden; background: var(--white); }
  .flyer {
    position: relative;
    width: 1200px;
    height: 1200px;
    overflow: hidden;
    font-family: "Arimo", Arial, sans-serif;
  }
  .age-band {
    position: absolute; left: 0; top: 0; width: 1200px; height: 153px;
    background: var(--band-grey);
    display: flex; align-items: center; justify-content: center;
  }
  .age-question {
    font-family: "Luckiest Guy", "Arial Black", sans-serif;
    font-size: 112px;
    line-height: 1;
    color: var(--ink);
    letter-spacing: 2px;
    -webkit-text-stroke: 0;
    text-shadow: 0 0 0 var(--white), 4px 4px 0 var(--white), -3px -3px 0 var(--white), 3px -3px 0 var(--white), -3px 3px 0 var(--white);
    padding-top: 14px;
  }
  .age-question .small-word { font-size: 68px; margin: 0 14px; }
  .beach-scene {
    position: absolute; left: 0; top: 153px; width: 1200px; height: 838px;
    background:
      linear-gradient(180deg, var(--sky-light) 0%, #fbf1c6 35%, var(--sky-warm) 60%, #f3e3b0 72%, var(--sand) 100%);
  }
  .headline {
    position: absolute; left: 82px; top: 210px;
    font-size: 53px; font-weight: 400; line-height: 1.2;
    color: var(--ink); text-transform: uppercase; letter-spacing: 0.5px;
  }
  .headline .highlight { color: var(--accent-red); font-weight: 700; }
  .benefits {
    position: absolute; right: 58px; top: 404px;
    list-style: none; text-align: right;
  }
  .benefits li {
    font-size: 29px; font-weight: 700; font-style: italic;
    color: var(--list-ink); line-height: 45.5px;
    display: flex; align-items: center; justify-content: flex-end; gap: 10px;
  }
  .benefits .tick { width: 26px; height: 26px; flex: none; }
  .cash-options {
    position: absolute; right: 60px; top: 813px;
    text-align: right; font-size: 22px; font-weight: 700;
    line-height: 36px; color: var(--cash-ink);
  }
  .footer-shapes { position: absolute; left: 0; top: 990px; }
  .consult {
    position: absolute; left: 0; top: 1012px; width: 512px;
    text-align: center; color: var(--ink); font-weight: 700;
  }
  .consult .invite { font-size: 29px; line-height: 38px; }
  .consult .phone { font-size: 49px; line-height: 64px; }
  .company {
    position: absolute; left: 520px; top: 1025px; width: 736px;
    text-align: center; color: var(--white); font-weight: 700;
    padding-right: 60px;
  }
  .company .name { font-size: 31px; line-height: 40px; }
  .company .license { font-size: 17px; line-height: 30px; }
  .company .web { font-size: 24px; line-height: 34px; margin-top: 26px; }
</style>
</head>
<body>
<main class="flyer">
  <header class="age-band">
    <h1 class="age-question">62<span class="small-word">OR</span>OLDER?</h1>
  </header>

  <div class="beach-scene" role="img" aria-label="Smiling senior couple in white clothes embracing on a sunlit beach at sunset"></div>

  <h2 class="headline">A <span class="highlight">Reverse Mortgage</span> could be<br>your road to <span class="highlight">Financial Freedom</span></h2>

  <ul class="benefits">
    <li><svg class="tick" viewBox="0 0 26 26" aria-hidden="true"><rect x="2" y="5" width="18" height="18" fill="none" stroke="var(--tick-blue)" stroke-width="2"/><path d="M6 13 l5 5 l12 -15" fill="none" stroke="var(--tick-blue)" stroke-width="3"/></svg>No Monthly Payments</li>
    <li><svg class="tick" viewBox="0 0 26 26" aria-hidden="true"><rect x="2" y="5" width="18" height="18" fill="none" stroke="var(--tick-blue)" stroke-width="2"/><path d="M6 13 l5 5 l12 -15" fill="none" stroke="var(--tick-blue)" stroke-width="3"/></svg>No Income Requirements</li>
    <li><svg class="tick" viewBox="0 0 26 26" aria-hidden="true"><rect x="2" y="5" width="18" height="18" fill="none" stroke="var(--tick-blue)" stroke-width="2"/><path d="M6 13 l5 5 l12 -15" fill="none" stroke="var(--tick-blue)" stroke-width="3"/></svg>No Credit Score Requirements</li>
    <li><svg class="tick" viewBox="0 0 26 26" aria-hidden="true"><rect x="2" y="5" width="18" height="18" fill="none" stroke="var(--tick-blue)" stroke-width="2"/><path d="M6 13 l5 5 l12 -15" fill="none" stroke="var(--tick-blue)" stroke-width="3"/></svg>No Loss of Ownership</li>
  </ul>

  <p class="cash-options">Receive Cash by<br>Lumpsum, Monthly Installments<br>or a Line of credit!!</p>

  <svg class="footer-shapes" width="1200" height="210" viewBox="0 0 1200 210" aria-hidden="true">
    <rect x="0" y="0" width="1200" height="210" fill="var(--footer-grey)"/>
    <polygon points="528,0 552,0 520,210 496,210" fill="var(--footer-stripe)"/>
    <polygon points="552,0 1200,0 1200,210 520,210" fill="var(--footer-dark)"/>
  </svg>

  <section class="consult">
    <p class="invite">Call us today<br>for a Free Consultation!!</p>
    <p class="phone">(800) 471-2965</p>
  </section>

  <section class="company">
    <p class="name">Bluegate Financial Services, Inc.</p>
    <p class="license">NMLS #318760</p>
    <p class="web">www.bluegatehome.com</p>
  </section>
</main>
</body>
</html>
```